Tallow Creek Architectural Systems Business Card

We have a logo - but we need a business card. We are a specialty manufacturer of wood wall and ceiling panels. Please visit our website - www.tallowcreekas.com to see examples of our products.
We create wood architectural systems - so we would love to see wood on the card somehow. Maybe something similar to our grille system?
We would like a spot on the business card for a QR code that people can scan to add the contact to their phone (we have the QR codes - just need a spot on the card).
As for the contact info - we want to keep it simple. (Name, Cell phone, Fax, email, website)

Target Market(s)

Architects and general contractors

Industry/Entity Type

Construction

Contact Information for Business Card

Name, Cell phone, fax, email, website

Requirements
Must have
• space for a QR code, wood feature
Nice to have
• We just want something a little different - but not too crazy. We want to stand out - but in a professional way.
Should not have
• nothing too busy

```html
<!DOCTYPE html>
<html lang="en">
<head>
<meta charset="utf-8">
<title>Tallow Creek Architectural Systems – Business Card</title>
<link rel="stylesheet" href="https://fonts.googleapis.com/css2?family=Carlito:wght@400;700&display=swap">
<style>
  :root {
    --red: #b00404;
    --ink: #1f1f1f;
    --charcoal: #2d2b2c;
    --paper: #ffffff;
    --wood-light: #eec08f;
    --wood-mid: #e1aa6e;
    --wood-dark: #d39a5c;
  }
  * { box-sizing: border-box; margin: 0; padding: 0; }
  html, body { width: 887px; height: 1200px; overflow: hidden; background: var(--paper); }
  body { font-family: "Carlito", "Calibri", sans-serif; }
  .canvas { position: relative; width: 887px; height: 1200px; background: var(--paper); }

  .edge { position: absolute; left: 0; width: 887px; background: var(--charcoal); }
  .edge--top { top: 0; height: 4px; }
  .edge--bottom { bottom: 0; height: 6px; }

  /* Front */
  .front { position: absolute; top: 0; left: 0; width: 887px; height: 578px; }
  .front__wood {
    position: absolute; top: 4px; left: 0; width: 887px; height: 548px;
    background:
      repeating-linear-gradient(90deg, rgba(160,100,40,0.18) 0 1px, transparent 1px 74px),
      linear-gradient(90deg, var(--wood-light), var(--wood-mid) 30%, var(--wood-light) 55%, var(--wood-dark) 80%, var(--wood-light));
  }
  .front__brand {
    position: absolute; top: 228px; left: 0; width: 887px;
    display: flex; align-items: center; justify-content: center; gap: 16px;
  }
  .brand-mark { width: 34px; height: 34px; background: var(--red); flex: none; }
  .brand-name { color: var(--red); font-weight: 700; line-height: 1; }
  .front .brand-name { font-size: 44px; }
  .front__web {
    position: absolute; top: 520px; left: 0; width: 887px;
    display: flex; align-items: center;
  }
  .front__rule { height: 2px; background: var(--red); flex: 1; }
  .front__url { color: var(--paper); font-size: 22px; letter-spacing: 0.5px; padding: 0 14px; white-space: nowrap; }
  .front__tab { position: absolute; top: 552px; left: 277px; width: 333px; height: 26px; background: var(--red); }

  .divider { position: absolute; top: 578px; left: 0; width: 887px; height: 41px; background: var(--charcoal); }

  /* Back */
  .back { position: absolute; top: 619px; left: 0; width: 887px; height: 575px; }
  .back__brand {
    position: absolute; top: 90px; left: 502px; width: 330px;
    display: flex; align-items: center; gap: 12px;
  }
  .back .brand-mark { width: 26px; height: 26px; }
  .back .brand-name { font-size: 30px; }
  .holder { position: absolute; top: 95px; left: 56px; font-size: 40px; color: var(--red); letter-spacing: 0.5px; }
  .holder__first { font-weight: 700; }
  .holder__last { font-weight: 400; }
  .contacts { position: absolute; top: 191px; left: 54px; list-style: none; }
  .contact { display: flex; align-items: center; height: 52px; font-size: 20px; color: var(--ink); letter-spacing: 0.3px; }
  .contact__icon { width: 32px; height: 32px; margin-right: 12px; fill: var(--red); flex: none; }
  .back__band { position: absolute; top: 445px; left: 0; width: 887px; height: 22px; background: var(--red); }
  .qr-spot {
    position: absolute; top: 378px; left: 636px; width: 146px; height: 144px;
    background: var(--paper); border: 3px solid var(--red);
  }
</style>
</head>
<body>
<main class="canvas">
  <div class="edge edge--top"></div>

  <section class="front">
    <div class="front__wood" role="img" aria-label="Light pine wood panelling background"></div>
    <div class="front__brand">
      <span class="brand-mark"></span>
      <span class="brand-name">Tallow Creek Architectural Systems</span>
    </div>
    <div class="front__web">
      <span class="front__rule"></span>
      <span class="front__url">www.tallowcreekas.com</span>
      <span class="front__rule"></span>
    </div>
    <div class="front__tab"></div>
  </section>

  <div class="divider"></div>

  <section class="back">
    <div class="back__brand">
      <span class="brand-mark"></span>
      <span class="brand-name">Tallow Creek Architectural Systems</span>
    </div>

    <h1 class="holder"><span class="holder__first">NAME</span> <span class="holder__last">HERE</span></h1>

    <ul class="contacts">
      <li class="contact">
        <svg class="contact__icon" viewBox="0 0 32 32" aria-hidden="true"><path d="M6 3c2-1 3 0 4 1l4 6c1 1 0 3-1 4l-2 1c1 3 4 6 7 7l1-2c1-1 3-2 4-1l6 4c1 1 2 2 1 4-2 3-4 4-7 3C13 27 5 19 3 10 2 7 3 5 6 3z"/></svg>
        <span>+0123-456-789</span>
      </li>
      <li class="contact">
        <svg class="contact__icon" viewBox="0 0 32 32" aria-hidden="true"><rect x="8" y="2" width="16" height="8"/><rect x="1" y="11" width="30" height="13" rx="2"/><rect x="7" y="20" width="18" height="11" fill="#fff" stroke="#b00404" stroke-width="2"/><path d="M10 24h12M10 27h12" stroke="#b00404" stroke-width="1.5"/></svg>
        <span>+0123-456-789</span>
      </li>
      <li class="contact">
        <svg class="contact__icon" viewBox="0 0 32 32" aria-hidden="true"><text x="16" y="27" text-anchor="middle" font-family="Arial, sans-serif" font-weight="700" font-size="34" fill="#b00404">@</text></svg>
        <span>name@tallowcreekas.com</span>
      </li>
      <li class="contact">
        <svg class="contact__icon" viewBox="0 0 32 32" aria-hidden="true"><circle cx="16" cy="16" r="15"/><g fill="none" stroke="#fff" stroke-width="1.4"><ellipse cx="16" cy="16" rx="6" ry="15"/><path d="M16 1v30M1 16h30M4 8h24M4 24h24"/></g></svg>
        <span>www.tallowcreekas.com</span>
      </li>
    </ul>

    <div class="back__band"></div>
    <div class="qr-spot" aria-label="Space for contact QR code"></div>
  </section>

  <div class="edge edge--bottom"></div>
</main>
</body>
</html>
```